Business Card Design Project

Name of Company: Barwinek Coaching & Consulting
Possible Acronym: Barwinek
My Name: Lorelei Barwinek, LL.B.
My email address: lorelei@barwinekconsulting.example
My tel.: +44 (0) 7834 629 058
My skype address: barwinekbc
I am offering executive coaching and consulting in the area of business development and strategic planning to intellectual property law firms around the world.
Since I will be marketing to the legal industry, the card must be fairly conservative. However I want it to also have flare and spark. I want to convey to potential clients that I can be the spark that will ignite their potential. I like the combination of navy blue and hot pink. However, I have decided that hot pink is not corporate enough so I would like to use a colour with navy that comes close to hot pink but is more conservative. Not red. I would consider swapping navy blue for grey if you thought that would look better. I would like the background of the card to be entirely white - both back and front - only the letters will be in colour.
I would like the card to be double sided with the name of my firm (or the acronym) and my email address underneath (lorelei@barwinekconsulting.example) on the back and on the front, all of the information above.
With gratitude!
Lorelei

```html
<!DOCTYPE html>
<html lang="en">
<head>
<meta charset="utf-8">
<title>Barwinek Coaching &amp; Consulting – Business Cards</title>
<link rel="stylesheet" href="https://fonts.googleapis.com/css2?family=Questrial&display=swap">
<style>
  :root {
    --navy: #1f3282;
    --paper: #fcfcf9;
    --stage: #e6e7ea;
    --muted: #9a9a9a;
    --card-w: 500px;
    --card-h: 286px;
  }
  * { box-sizing: border-box; margin: 0; padding: 0; }
  html, body {
    width: 1200px; height: 960px; overflow: hidden;
    background: var(--stage);
    font-family: "Questrial", "Century Gothic", sans-serif;
  }
  .sheet { position: relative; width: 1200px; height: 960px; }

  .card {
    position: absolute;
    width: var(--card-w); height: var(--card-h);
    background: var(--paper);
    color: var(--navy);
    overflow: hidden;
    box-shadow: 0 2px 6px rgba(0,0,0,.18);
  }
  .card--back-navy { left: 70px; top: 90px; background: var(--navy); color: #fff; }
  .card--front { left: 630px; top: 90px; }
  .card--back-white { left: 350px; top: 560px; }

  .brand-mark {
    position: absolute; left: 0; right: 0;
    display: flex; align-items: center; justify-content: center; gap: 10px;
    font-size: 36px; line-height: 1;
  }
  .brand-mark__square { width: 14px; height: 14px; background: currentColor; }

  .company-name {
    position: absolute; left: 0; right: 0; text-align: center; white-space: nowrap;
  }

  /* Navy back */
  .card--back-navy .brand-mark { top: 76px; }
  .card--back-navy .company-name { top: 152px; font-size: 22px; }
  .card--back-navy .email-band {
    position: absolute; left: 0; right: 0; top: 220px; height: 30px;
    background: var(--paper); color: var(--navy);
    font-size: 16px; line-height: 30px; text-align: right; padding-right: 12px;
  }

  /* Front */
  .card--front .brand-mark { top: 42px; }
  .card--front .company-name { top: 102px; font-size: 17px; }
  .contact-block {
    position: absolute; top: 182px; left: 0; right: 0;
    display: flex; justify-content: center; align-items: center;
  }
  .person { text-align: right; padding-right: 16px; white-space: nowrap; }
  .person__name { font-size: 16px; }
  .person__role { font-size: 14px; color: var(--muted); }
  .contact-divider { width: 3px; height: 50px; background: var(--navy); flex: none; }
  .contact-list { list-style: none; padding-left: 16px; font-size: 11px; line-height: 18px; white-space: nowrap; }
  .card--front .footer-band {
    position: absolute; left: 0; right: 0; bottom: 6px; height: 11px; background: var(--navy);
  }

  /* White back */
  .card--back-white .brand-mark { top: 70px; }
  .card--back-white .company-name { top: 146px; font-size: 22px; }
  .card--back-white .email-band {
    position: absolute; left: 0; right: 0; top: 220px; height: 30px;
    background: var(--navy); color: #fff;
    font-size: 16px; line-height: 30px; text-align: right; padding-right: 10px;
  }
</style>
</head>
<body>
<main class="sheet">

  <section class="card card--back-navy" aria-label="Card back, navy">
    <div class="brand-mark"><span class="brand-mark__square"></span>Barwinek</div>
    <p class="company-name">Barwinek Coaching &amp; Consulting</p>
    <p class="email-band">lorelei@barwinekconsulting.example</p>
  </section>

  <section class="card card--front" aria-label="Card front">
    <div class="brand-mark"><span class="brand-mark__square"></span>Barwinek</div>
    <p class="company-name">Barwinek Coaching &amp; Consulting</p>
    <div class="contact-block">
      <div class="person">
        <p class="person__name">Lorelei Barwinek, LL.B.</p>
        <p class="person__role">owner</p>
      </div>
      <span class="contact-divider"></span>
      <ul class="contact-list">
        <li>Phone : +44 (0) 7834 629 058</li>
        <li>email : lorelei@barwinekconsulting.example</li>
        <li>Skype : barwinekbc</li>
      </ul>
    </div>
    <div class="footer-band"></div>
  </section>

  <section class="card card--back-white" aria-label="Card back, white">
    <div class="brand-mark"><span class="brand-mark__square"></span>Barwinek</div>
    <p class="company-name">Barwinek Coaching &amp; Consulting</p>
    <p class="email-band">lorelei@barwinekconsulting.example</p>
  </section>

</main>
</body>
</html>
```